Website redesign for Ka-Strata, a leading semiconductor design company

I have an existing website design created in Figma, but I am looking for a completely new and more professional design with a stronger user experience (UX) and modern visual style. The new design should maintain the same text content, not exact text, page purposes, and sections, but the entire UI should be redesigned from scratch. The website should be fully coded and developed. The website is about 10 pages in total.
Scope of Work
1. UI/UX Redesign
Create new, modern, and professional designs for all pages.

Use the existing Figma file ONLY for but we are open for new and innovative ideas:
Text content Not exact text
Propose professional and catchy text
Page purposes
Sections
Visual design must be fully new, not a modification of the current layout.
Primary color palette: Blue & White
You are free to add complementary colors to improve aesthetics and usability.

Design must follow best practices for:
User experience
Visual hierarchy
Accessibility
Readability

2. Responsive Design
The entire website must be designed and developed to work perfectly on:
Desktop (all screen sizes)
Tablets (portrait & landscape)
Mobile Phones (all screen sizes)
Responsive layouts must be customized, not simply scaled.

3. Website Development
Convert the final approved design into a fully functional website.
Clean, modern, and maintainable code.
Technologies HTML/CSS/Javascript - Native design not using platforms such as wordpress
Fast-loading pages, SEO-friendly structure.
Content API Structured
AI-Optimized Content Layout
Functionality such as form submission (contact us) or email composing (careers)
Integrate any needed animations or interactions.
Ensure cross-browser compatibility.
Deliverables
Fully redesigned UI for all pages (in Figma or similar).
Fully responsive front-end development.
Deployment-ready codebase.
Source files for both design and code.

Files to be shared
Current design files (png/pdf format)
Current figma design
Pages structure
Pages content

```html
<!DOCTYPE html>
<html lang="en">
<head>
<meta charset="UTF-8">
<title>Ka-Strata — Dark and White Theme Homepage</title>
<link href="https://fonts.googleapis.com/css2?family=Outfit:wght@400;500;600;700&display=swap" rel="stylesheet">
<style>
  :root{
    --canvas:#ffffff;
    --label:#111111;
  }
  .theme-dark{
    --bg:#05080c; --band:#0a1117; --card:#0f1820; --line:#1b2832;
    --text:#ffffff; --muted:#8c99a6; --accent:#1ec3e8; --accent-deep:#0b86b8;
    --photo-a:#2a3b48; --photo-b:#111a22; --foot:#05080c; --foot-text:#ffffff; --foot-muted:#7f8d9a;
  }
  .theme-light{
    --bg:#ffffff; --band:#f3f7fa; --card:#ffffff; --line:#dfe7ee;
    --text:#0b1a2b; --muted:#5e6c7b; --accent:#17a8da; --accent-deep:#0b7fb3;
    --photo-a:#c9d5df; --photo-b:#7d8f9f; --foot:#0d1a30; --foot-text:#ffffff; --foot-muted:#8c9bb0;
  }
  *{box-sizing:border-box;margin:0;padding:0}
  html,body{width:738px;height:1200px;overflow:hidden}
  body{background:var(--canvas);font-family:"Outfit",sans-serif;position:relative}
  .theme-label{position:absolute;top:14px;width:325px;text-align:center;font-size:15px;font-weight:700;color:var(--label)}
  .theme-label.left{left:25px}.theme-label.right{left:388px}
  .page{position:absolute;top:70px;width:325px;height:1100px;background:var(--bg);color:var(--text);display:flex;flex-direction:column;overflow:hidden;box-shadow:0 0 0 1px #e3e3e3}
  .page.theme-dark{left:25px}.page.theme-light{left:388px}
  .section-title{font-size:10px;font-weight:700;text-align:center}
  .btn{display:inline-block;background:var(--accent);color:#fff;font-size:4.5px;font-weight:600;padding:3px 7px;border-radius:3px}
  .btn.ghost{background:transparent;border:0.6px solid var(--accent);color:var(--accent)}
  .photo{background:linear-gradient(135deg,var(--photo-a),var(--photo-b));border-radius:4px}

  .site-header{height:24px;display:flex;align-items:center;justify-content:space-between;padding:0 12px;border-bottom:0.6px solid var(--line)}
  .brand{display:flex;align-items:center;gap:3px;font-size:6px;font-weight:700;color:var(--text)}
  .brand-mark{width:6px;height:6px;background:var(--accent);border-radius:1px}
  .main-nav{display:flex;gap:8px;font-size:4px;color:var(--muted)}

  .hero{height:150px;display:flex;align-items:center;gap:10px;padding:0 14px}
  .hero-copy{flex:1}
  .hero-title{font-size:17px;font-weight:700;line-height:1.08}
  .hero-title em{font-style:normal;color:var(--accent)}
  .hero-text{font-size:4.5px;color:var(--muted);line-height:1.5;margin:7px 0;max-width:120px}
  .hero-actions{display:flex;gap:4px}
  .hero-photo{width:132px;height:92px}

  .capabilities{height:148px;padding:18px 14px 0;background:var(--band)}
  .cap-grid{display:flex;gap:7px;margin-top:14px}
  .cap-card{flex:1;height:64px;background:var(--card);border:0.6px solid var(--line);border-radius:4px;padding:9px 7px}
  .cap-icon{width:10px;height:10px;border-radius:2px;background:var(--accent);opacity:.85;margin-bottom:6px}
  .cap-title{font-size:5px;font-weight:600}
  .cap-text{font-size:4px;color:var(--muted);line-height:1.4;margin-top:3px}

  .industries{height:180px;padding:22px 0 0}
  .ind-row{display:flex;gap:6px;margin-top:16px;align-items:center;padding-left:6px}
  .ind-photo{position:relative;height:96px}
  .ind-photo.side{width:60px;height:86px}
  .ind-photo.main{width:176px;height:100px}
  .ind-caption{position:absolute;left:6px;bottom:5px;font-size:4.5px;font-weight:600;color:#fff}

  .knowledge{height:162px;padding:14px 14px 0;background:var(--band)}
  .know-grid{display:flex;gap:7px;margin-top:12px}
  .know-card{flex:1;background:var(--card);border:0.6px solid var(--line);border-radius:4px;overflow:hidden}
  .know-card .photo{height:52px;border-radius:0}
  .know-body{padding:5px 6px 7px}
  .know-title{font-size:5px;font-weight:600;line-height:1.3}
  .know-link{font-size:4px;color:var(--accent);margin-top:4px}

  .academy{height:160px;padding:18px 14px 0;display:flex;gap:10px}
  .academy-copy{flex:1}
  .academy .section-title{text-align:left}
  .track{display:flex;gap:5px;align-items:flex-start;border:0.6px solid var(--line);background:var(--card);border-radius:3px;padding:4px 5px;margin-top:5px}
  .track-dot{width:6px;height:6px;border-radius:50%;background:var(--accent);flex:none;margin-top:1px}
  .track-name{font-size:4.5px;font-weight:600}
  .track-text{font-size:3.8px;color:var(--muted)}
  .stats{display:flex;gap:12px;margin-top:7px}
  .stat-value{font-size:9px;font-weight:700;color:var(--accent)}
  .stat-label{font-size:3.8px;color:var(--muted)}
  .academy-photo{width:130px;height:92px;margin-top:20px}

  .careers{height:148px;padding:20px 0 0;background:var(--band);text-align:center}
  .job{width:200px;margin:7px auto 0;display:flex;justify-content:space-between;align-items:center;text-align:left;background:var(--card);border:0.6px solid var(--line);border-radius:4px;padding:7px 8px}
  .job:first-of-type{margin-top:14px}
  .job-title{font-size:5px;font-weight:600}
  .job-meta{font-size:3.8px;color:var(--muted);margin-top:2px}
  .careers .btn.ghost{margin-top:10px}

  .site-footer{height:128px;background:var(--foot);color:var(--foot-text);padding:16px 14px 0;display:flex;flex-direction:column}
  .foot-grid{display:flex;gap:14px}
  .foot-brand{flex:1.5}
  .foot-brand .brand{color:var(--foot-text)}
  .foot-text{font-size:4px;color:var(--foot-muted);margin:5px 0;max-width:80px;line-height:1.4}
  .socials{display:flex;gap:3px}
  .socials span{width:7px;height:7px;border-radius:50%;border:0.6px solid var(--foot-muted)}
  .foot-col{flex:1}
  .foot-head{font-size:4.5px;font-weight:600;margin-bottom:4px}
  .foot-col p{font-size:3.8px;color:var(--foot-muted);margin-bottom:3px}
  .copyright{margin-top:auto;border-top:0.6px solid #1f2d3b;font-size:3.8px;color:var(--foot-muted);text-align:center;padding:7px 0}
</style>
</head>
<body>
<div class="theme-label left">Dark Theme</div>
<div class="theme-label right">White Theme</div>

<main class="page theme-dark">
  <header class="site-header">
    <div class="brand"><span class="brand-mark"></span>Ka-Strata</div>
    <nav class="main-nav"><span>Home</span><span>About</span><span>Solutions</span><span>Industries</span><span>Careers</span></nav>
    <span class="btn">Contact Us</span>
  </header>
  <section class="hero">
    <div class="hero-copy">
      <h1 class="hero-title">Your AI-<br>Augmented<br><em>Innovation<br>Partner</em></h1>
      <p class="hero-text">Custom silicon and AI design services that carry your chip from spec to tape-out.</p>
      <div class="hero-actions"><span class="btn">Explore More</span><span class="btn ghost">Talk to Us</span></div>
    </div>
    <div class="photo hero-photo" role="img" aria-label="Engineers at a desk with laptops and circuit boards"></div>
  </section>
  <section class="capabilities">
    <h2 class="section-title">Core Capabilities</h2>
    <div class="cap-grid">
      <div class="cap-card"><div class="cap-icon"></div><div class="cap-title">End-to-End IC</div><p class="cap-text">Full flow from architecture to tape-out.</p></div>
      <div class="cap-card"><div class="cap-icon"></div><div class="cap-title">High-Quality Verification</div><p class="cap-text">Rigorous checks that catch bugs early.</p></div>
      <div class="cap-card"><div class="cap-icon"></div><div class="cap-title">Industry Compliance</div><p class="cap-text">Built to meet safety and quality standards.</p></div>
    </div>
  </section>
  <section class="industries">
    <h2 class="section-title">Industries We Serve</h2>
    <div class="ind-row">
      <div class="photo ind-photo side" role="img" aria-label="Robotic arm in a lab"><span class="ind-caption">Automotive</span></div>
      <div class="photo ind-photo main" role="img" aria-label="Earth at night seen from orbit"><span class="ind-caption">Space Systems</span></div>
      <div class="photo ind-photo side" role="img" aria-label="Server racks in a data hall"><span class="ind-caption">Data Centers</span></div>
    </div>
  </section>
  <section class="knowledge">
    <h2 class="section-title">Knowledge Center</h2>
    <div class="know-grid">
      <article class="know-card"><div class="photo" role="img" aria-label="Close-up of a microchip"></div><div class="know-body"><div class="know-title">How AI Is Reshaping the Chip Design Flow</div><div class="know-link">Read More</div></div></article>
      <article class="know-card"><div class="photo" role="img" aria-label="Team reviewing designs on screens"></div><div class="know-body"><div class="know-title">Bridging the Gap From Spec to Silicon</div><div class="know-link">Read More</div></div></article>
      <article class="know-card"><div class="photo" role="img" aria-label="Wafer under blue light"></div><div class="know-body"><div class="know-title">Advanced Packaging Trends for 2025</div><div class="know-link">Read More</div></div></article>
    </div>
  </section>
  <section class="academy">
    <div class="academy-copy">
      <h2 class="section-title">Ka-Strata Academy</h2>
      <div class="track"><span class="track-dot"></span><div><div class="track-name">Verification Program</div><div class="track-text">Hands-on training with industry mentors.</div></div></div>
      <div class="track"><span class="track-dot"></span><div><div class="track-name">Physical Design Track</div><div class="track-text">Hands-on training with industry mentors.</div></div></div>
      <div class="track"><span class="track-dot"></span><div><div class="track-name">Analog Layout Course</div><div class="track-text">Hands-on training with industry mentors.</div></div></div>
      <div class="stats"><div><div class="stat-value">180+</div><div class="stat-label">Graduates</div></div><div><div class="stat-value">95%</div><div class="stat-label">Hiring Rate</div></div></div>
    </div>
    <div class="photo academy-photo" role="img" aria-label="Students working together in a classroom"></div>
  </section>
  <section class="careers">
    <h2 class="section-title">Build Your Future With Us</h2>
    <div class="job"><div><div class="job-title">Senior RTL Design Engineer</div><div class="job-meta">Hybrid · Full-time</div></div><span class="btn">Apply</span></div>
    <div class="job"><div><div class="job-title">DFT / Physical Design Team Lead</div><div class="job-meta">Hybrid · Full-time</div></div><span class="btn">Apply</span></div>
    <span class="btn ghost">View All Jobs</span>
  </section>
  <footer class="site-footer">
    <div class="foot-grid">
      <div class="foot-brand"><div class="brand"><span class="brand-mark"></span>Ka-Strata</div><p class="foot-text">Designing the silicon that powers tomorrow.</p><div class="socials"><span></span><span></span><span></span><span></span></div></div>
      <div class="foot-col"><div class="foot-head">Company</div><p>About Us</p><p>Careers</p><p>News</p></div>
      <div class="foot-col"><div class="foot-head">Solutions</div><p>Design</p><p>Verification</p><p>Academy</p></div>
      <div class="foot-col"><div class="foot-head">Contact</div><p>Send a Message</p><p>Office Hours</p><p>Support</p></div>
    </div>
    <div class="copyright">© 2025 Ka-Strata. All rights reserved.</div>
  </footer>
</main>

<main class="page theme-light">
  <header class="site-header">
    <div class="brand"><span class="brand-mark"></span>Ka-Strata</div>
    <nav class="main-nav"><span>Home</span><span>About</span><span>Solutions</span><span>Industries</span><span>Careers</span></nav>
    <span class="btn">Contact Us</span>
  </header>
  <section class="hero">
    <div class="hero-copy">
      <h1 class="hero-title">Your AI-<br>Augmented<br><em>Innovation<br>Partner</em></h1>
      <p class="hero-text">Custom silicon and AI design services that carry your chip from spec to tape-out.</p>
      <div class="hero-actions"><span class="btn">Explore More</span><span class="btn ghost">Talk to Us</span></div>
    </div>
    <div class="photo hero-photo" role="img" aria-label="Engineers at a desk with laptops and circuit boards"></div>
  </section>
  <section class="capabilities">
    <h2 class="section-title">Core Capabilities</h2>
    <div class="cap-grid">
      <div class="cap-card"><div class="cap-icon"></div><div class="cap-title">End-to-End IC</div><p class="cap-text">Full flow from architecture to tape-out.</p></div>
      <div class="cap-card"><div class="cap-icon"></div><div class="cap-title">High-Quality Verification</div><p class="cap-text">Rigorous checks that catch bugs early.</p></div>
      <div class="cap-card"><div class="cap-icon"></div><div class="cap-title">Industry Compliance</div><p class="cap-text">Built to meet safety and quality standards.</p></div>
    </div>
  </section>
  <section class="industries">
    <h2 class="section-title">Industries We Serve</h2>
    <div class="ind-row">
      <div class="photo ind-photo side" role="img" aria-label="Robotic arm in a lab"><span class="ind-caption">Automotive</span></div>
      <div class="photo ind-photo main" role="img" aria-label="Earth at night seen from orbit"><span class="ind-caption">Space Systems</span></div>
      <div class="photo ind-photo side" role="img" aria-label="Server racks in a data hall"><span class="ind-caption">Data Centers</span></div>
    </div>
  </section>
  <section class="knowledge">
    <h2 class="section-title">Knowledge Center</h2>
    <div class="know-grid">
      <article class="know-card"><div class="photo" role="img" aria-label="Close-up of a microchip"></div><div class="know-body"><div class="know-title">How AI Is Reshaping the Chip Design Flow</div><div class="know-link">Read More</div></div></article>
      <article class="know-card"><div class="photo" role="img" aria-label="Team reviewing designs on screens"></div><div class="know-body"><div class="know-title">Bridging the Gap From Spec to Silicon</div><div class="know-link">Read More</div></div></article>
      <article class="know-card"><div class="photo" role="img" aria-label="Wafer under blue light"></div><div class="know-body"><div class="know-title">Advanced Packaging Trends for 2025</div><div class="know-link">Read More</div></div></article>
    </div>
  </section>
  <section class="academy">
    <div class="academy-copy">
      <h2 class="section-title">Ka-Strata Academy</h2>
      <div class="track"><span class="track-dot"></span><div><div class="track-name">Verification Program</div><div class="track-text">Hands-on training with industry mentors.</div></div></div>
      <div class="track"><span class="track-dot"></span><div><div class="track-name">Physical Design Track</div><div class="track-text">Hands-on training with industry mentors.</div></div></div>
      <div class="track"><span class="track-dot"></span><div><div class="track-name">Analog Layout Course</div><div class="track-text">Hands-on training with industry mentors.</div></div></div>
      <div class="stats"><div><div class="stat-value">180+</div><div class="stat-label">Graduates</div></div><div><div class="stat-value">95%</div><div class="stat-label">Hiring Rate</div></div></div>
    </div>
    <div class="photo academy-photo" role="img" aria-label="Students working together in a classroom"></div>
  </section>
  <section class="careers">
    <h2 class="section-title">Build Your Future With Us</h2>
    <div class="job"><div><div class="job-title">Senior RTL Design Engineer</div><div class="job-meta">Hybrid · Full-time</div></div><span class="btn">Apply</span></div>
    <div class="job"><div><div class="job-title">DFT / Physical Design Team Lead</div><div class="job-meta">Hybrid · Full-time</div></div><span class="btn">Apply</span></div>
    <span class="btn ghost">View All Jobs</span>
  </section>
  <footer class="site-footer">
    <div class="foot-grid">
      <div class="foot-brand"><div class="brand"><span class="brand-mark"></span>Ka-Strata</div><p class="foot-text">Designing the silicon that powers tomorrow.</p><div class="socials"><span></span><span></span><span></span><span></span></div></div>
      <div class="foot-col"><div class="foot-head">Company</div><p>About Us</p><p>Careers</p><p>News</p></div>
      <div class="foot-col"><div class="foot-head">Solutions</div><p>Design</p><p>Verification</p><p>Academy</p></div>
      <div class="foot-col"><div class="foot-head">Contact</div><p>Send a Message</p><p>Office Hours</p><p>Support</p></div>
    </div>
    <div class="copyright">© 2025 Ka-Strata. All rights reserved.</div>
  </footer>
</main>
</body>
</html>
```